Land Buying Company Needs Letterhead for Direct Mail Marketing to Land Owners

We are looking for a professional letterhead that we will be including in our direct mail marketing. We will be sending this to land owners who may be interested in selling or purchasing land.

The letterhead needs to be editable. Headers and footers would look nice, but we are open. We would want it to include our address, website, phone, and email info. For right now the address to use for design purposes would the following:

Address: 415 Bramwell Avenue #600
Dallas, TX 75219
Website - www.quillridgeacres.example
Email - info@quillridgeacres.example
Phone - 866-402-ACRE

I have attached our logo zip file that we just had done on Pixel Guild. Let me know what questions you have, and thank you.

```html
<!DOCTYPE html>
<html lang="en">
<head>
<meta charset="utf-8">
<title>Quillridge Acres Letterhead</title>
<link rel="stylesheet" href="https://fonts.googleapis.com/css2?family=Jost:ital,wght@0,400;0,600;1,400&display=swap">
<style>
  :root {
    --backdrop: #f0f0f0;
    --paper: #e9eaeb;
    --forest: #465d2a;
    --lime: #8bc53f;
    --ink: #2b2b2b;
    --muted: #4a4a4a;
    --watermark: rgba(70, 93, 42, 0.14);
    --white: #ffffff;
  }
  * { margin: 0; padding: 0; box-sizing: border-box; }
  html, body { width: 1200px; height: 1200px; overflow: hidden; }
  body {
    position: relative;
    background: var(--backdrop);
    font-family: "Jost", sans-serif;
    color: var(--ink);
  }
  .letter-sheet {
    position: absolute;
    left: 81px; top: 241px;
    width: 488px; height: 684px;
    background: var(--paper);
    overflow: hidden;
  }
  .watermark-disc {
    position: absolute;
    left: 85px; top: 420px;
    width: 300px; height: 300px;
    border-radius: 50%;
    background: var(--watermark);
  }
  .brand {
    position: absolute;
    left: 50px; top: 45px;
    display: flex; align-items: center; gap: 8px;
  }
  .brand-dot {
    width: 32px; height: 32px; border-radius: 50%;
    background: var(--forest);
  }
  .brand-name {
    font-weight: 600; font-size: 17px; letter-spacing: 0.5px;
    color: var(--lime); line-height: 1.05; width: 120px;
  }
  .contact {
    position: absolute;
    left: 260px; top: 46px;
    list-style: none;
    font-size: 11.5px; color: var(--muted);
  }
  .contact li { display: flex; align-items: center; gap: 8px; height: 18px; }
  .contact svg { width: 12px; height: 12px; flex: none; }
  .recipient {
    position: absolute; left: 53px; top: 121px;
    font-size: 17px; color: var(--ink);
  }
  .letter-body {
    position: absolute; left: 50px; top: 168px;
    width: 380px;
    font-size: 16.4px; line-height: 22.3px;
    text-align: justify; color: var(--ink);
  }
  .closing {
    position: absolute; left: 62px; top: 544px;
    font-style: italic; font-size: 17px; color: var(--ink);
  }
  .signature {
    position: absolute; left: 48px; top: 578px;
    width: 223px; height: 46px;
    background: rgba(43, 43, 43, 0.08);
  }
  .web-band {
    position: absolute; left: 0; bottom: 0;
    width: 233px; height: 36px;
    background: var(--forest); color: var(--white);
    font-size: 13px; display: flex; align-items: center; padding-left: 14px;
  }
  .address {
    position: absolute; right: 29px; top: 632px;
    text-align: right; font-size: 13.5px; line-height: 19px; color: var(--muted);
  }
  .cover-sheet {
    position: absolute;
    left: 637px; top: 237px;
    width: 486px; height: 691px;
    background: var(--forest);
    display: flex; align-items: center; justify-content: center;
  }
  .cover-brand { display: flex; align-items: center; gap: 12px; }
  .cover-brand .brand-dot { width: 46px; height: 46px; background: var(--white); }
  .cover-brand .brand-name { color: var(--white); font-size: 24px; width: auto; }
</style>
</head>
<body>
  <section class="letter-sheet">
    <div class="watermark-disc"></div>
    <div class="brand">
      <span class="brand-dot"></span>
      <span class="brand-name">QUILLRIDGE ACRES</span>
    </div>
    <ul class="contact">
      <li><svg viewBox="0 0 12 12"><circle cx="6" cy="6" r="6" fill="#465d2a"/><path d="M4 3.2l1 1.3-.6.8a4 4 0 0 0 2.3 2.3l.8-.6 1.3 1-.6 1C6 8.8 3.2 6 3 4z" fill="#fff"/></svg>866-402-ACRE</li>
      <li><svg viewBox="0 0 12 12"><circle cx="6" cy="6" r="6" fill="#465d2a"/><rect x="3" y="4" width="6" height="4" fill="#fff"/></svg>info@quillridgeacres.example</li>
    </ul>
    <p class="recipient">TO</p>
    <p class="letter-body">Where does it come from? Contrary to popular belief, Lorem Ipsum is not simply random text. It has roots in a piece of classical Latin literature from 45 BC, making it over 2000 years old. Edwin Marlowe, a Latin professor at Ashgrove College in Virginia, looked up one of the more obscure Latin words, consectetur, from a Lorem Ipsum passage, and going through the cites of the word in classical literature, discovered the undoubtable source. Lorem Ipsum comes from sections 1.10.32 and 1.10.33 of "de Finibus Bonorum et Malorum" (The Extremes of Good and Evil) by Aurelian Tesk, written in 45 BC. This book is a treatise on the theory of ethics,</p>
    <p class="closing">Yours faithfully</p>
    <div class="signature" role="img" aria-label="Handwritten signature"></div>
    <div class="web-band">www.quillridgeacres.example</div>
    <address class="address" style="font-style:normal">415 Bramwell Avenue #600<br>Dallas, TX 75219</address>
  </section>

  <section class="cover-sheet">
    <div class="cover-brand">
      <span class="brand-dot"></span>
      <span class="brand-name">QUILLRIDGE ACRES</span>
    </div>
  </section>
</body>
</html>
```